Law School Textbook Rental Landing Page

We operate several law school bookstore websites. We need a single-page web landing page as the introduction page to our law school textbook rental program that we will be launching. The page should be simliar in style to the homepages of other textbook rental websites, such as www.plovarent.example, www.tamsileaf.example, www.quorridgeloans.example, http://www.brindelpages.example/rent-textbooks, etc.

The style is similar: an oversized search field, and different areas/icons promoting the benefits of the program, in our case the following:

Main message: "Save Up To 80% On Your Law School Textbooks!"

Secondary Messages:
-Save $$ On Your Textbooks!
-Easy & Free Rental Returns!
-1000s of Law Textbook Titles!
-30-Day Money Back Guarantee!
-Writing/Highlighting Allowed!

We'd prefer if most of the design would fit on a standard browser sized screen without the customer having to scroll down too much to see everything. We would need the final files in a HTML format.

Target Market(s)

The customers coming to this landing page are US law students, generally aged 21-28 years old looking to save money on their law school textbooks.

Industry/Entity Type

School

Requirements
Must have
• Must call out the following:

Secondary Messages:

```html
<!DOCTYPE html>
<html lang="en">
<head>
<meta charset="utf-8">
<title>Law School Textbook Rentals</title>
<link rel="stylesheet" href="https://fonts.googleapis.com/css2?family=Lato:wght@300;400;700;900&family=Cinzel:wght@400&display=swap">
<style>
  :root {
    --brand-red: #ba1f29;
    --headline-white: #ffffff;
    --accent-yellow: #f6f00c;
    --panel-outer: rgba(200, 200, 200, 0.55);
    --panel-inner: rgba(225, 225, 225, 0.82);
    --bullet-text: #4e4e4e;
    --cta-orange-top: #ffe31a;
    --cta-orange-bottom: #ff7c00;
    --cta-text: #6a2a00;
    --phone-green: #4a7a55;
    --phone-circle: #4fb32c;
  }
  * { margin: 0; padding: 0; box-sizing: border-box; }
  html, body { width: 1200px; height: 766px; overflow: hidden; background: var(--brand-red); }
  .page { position: relative; width: 1200px; height: 766px; background: var(--brand-red); font-family: "Lato", sans-serif; }

  .hero {
    position: absolute; left: 0; top: 133px; width: 1200px; height: 473px;
    background:
      radial-gradient(ellipse 300px 260px at 120px 260px, rgba(40, 34, 30, 0.85), transparent 70%),
      radial-gradient(ellipse 420px 200px at 650px 120px, rgba(120, 150, 100, 0.6), transparent 70%),
      radial-gradient(ellipse 260px 260px at 1080px 300px, rgba(170, 175, 180, 0.55), transparent 70%),
      linear-gradient(180deg, #6f8a4c 0%, #7a8e55 45%, #5e6c3c 75%, #4b5530 100%);
  }

  .book-stack {
    position: absolute; left: 231px; top: 189px; width: 240px; height: 374px;
    border-radius: 10px;
    background: linear-gradient(180deg, #2a9bc4 0%, #2d5fb8 14%, #9a1f9d 26%, #e5194f 38%, #ea3a20 48%, #f3d40e 60%, #f3e617 68%, #8fd42c 78%, #3bbf3a 88%, #23b6e6 100%);
  }

  .headline {
    position: absolute; left: 558px; top: 168px; width: 520px;
    color: var(--headline-white); font-weight: 400; font-size: 34px; line-height: 44px;
    letter-spacing: -0.2px;
  }
  .headline .highlight { color: var(--accent-yellow); font-size: 52px; font-weight: 400; letter-spacing: -1px; }

  .benefits-panel {
    position: absolute; left: 547px; top: 278px; width: 507px; height: 243px;
    border-radius: 22px; background: var(--panel-outer); padding: 9px;
  }
  .benefits-list {
    list-style: none; width: 100%; height: 100%; border-radius: 16px;
    background: var(--panel-inner); padding: 18px 0 0 34px;
  }
  .benefits-list li {
    display: flex; align-items: center; height: 40px;
    font-weight: 300; font-size: 26px; color: var(--bullet-text);
  }
  .benefits-list li::before {
    content: ""; width: 16px; height: 16px; margin-right: 24px; flex: none;
    border: 2px solid #666; background: radial-gradient(#555 0 30%, transparent 32%);
    background-size: 100% 100%;
    box-shadow: inset 0 0 0 3px #e6e6e6;
    background-color: #555;
  }

  .book-button {
    position: absolute; left: 579px; top: 544px; width: 207px; height: 46px;
    border-radius: 6px; border: none;
    background: linear-gradient(180deg, var(--cta-orange-top) 0%, #ffb400 40%, var(--cta-orange-bottom) 55%, #ff8a00 100%);
    color: var(--cta-text); font-family: "Lato", sans-serif; font-weight: 900; font-size: 18px;
    display: flex; align-items: center; justify-content: center;
    box-shadow: 0 2px 3px rgba(0,0,0,0.3);
  }

  .phone-pill {
    position: absolute; left: 850px; top: 537px; width: 181px; height: 46px;
    border-radius: 0 12px 12px 0; background: var(--phone-green);
    color: #fff; font-weight: 700; font-size: 20px;
    display: flex; align-items: center; padding-left: 45px;
  }
  .phone-badge { position: absolute; left: 798px; top: 521px; width: 78px; height: 78px; }

  .copyright {
    position: absolute; left: 0; top: 735px; width: 1200px; text-align: center;
    color: #fff; font-family: "Cinzel", serif; font-size: 11px; letter-spacing: 0.3px;
  }
</style>
</head>
<body>
<div class="page">
  <section class="hero" role="img" aria-label="Blurred photo of students in a green campus park"></section>

  <div class="book-stack" role="img" aria-label="Illustration of a colourful stack of textbooks"></div>

  <h1 class="headline">Save Up To <span class="highlight">80%</span> On Your Law School Textbooks!</h1>

  <div class="benefits-panel">
    <ul class="benefits-list">
      <li>Save $$ On Your Textbooks!</li>
      <li>Easy &amp; Free Rental Returns!</li>
      <li>1000s of Law Textbook Titles!</li>
      <li>30-Day Money Back Guarantee!</li>
      <li>Writing/Highlighting Allowed!</li>
    </ul>
  </div>

  <a class="book-button">BOOK NOW!</a>

  <div class="phone-pill">1 555 0142</div>
  <svg class="phone-badge" viewBox="0 0 78 78" aria-hidden="true">
    <defs>
      <radialGradient id="badgeFill" cx="40%" cy="30%" r="70%">
        <stop offset="0" stop-color="#8fe35a"/>
        <stop offset="0.6" stop-color="#45ad27"/>
        <stop offset="1" stop-color="#2d7f18"/>
      </radialGradient>
    </defs>
    <circle cx="39" cy="39" r="38" fill="#e9f3e4"/>
    <circle cx="39" cy="39" r="34" fill="url(#badgeFill)"/>
    <path d="M27 22c2-2 5-2 6 0l4 7c1 2 0 4-2 5l-3 2c2 5 6 9 11 11l2-3c1-2 3-3 5-2l7 4c2 1 2 4 0 6l-3 3c-3 3-9 3-16-2c-7-5-12-11-14-18c-1-5 0-9 3-13z" fill="#ffffff"/>
  </svg>

  <p class="copyright">Copyright © 2014 All Rights Reserved</p>
</div>
</body>
</html>
```